Zarqa Fowl "The Tender Path"

I need a business card design and a logo design for my business. It's a delivery business of halal poultry (chicken). I would the business card to include the following information.
-business name: Zarqa Fowl
-business tag line: "The Tender Path"
Name: Tariq Moussef
Contact number: 07812450937
E-mail: zarqa_fowl@mailbox-example.com
Website: www.zarqafowl-example.com
Also need a business logo also included relating to the business.
I would like it professional yet creative. Something original. I want it to have 2 main colours included.
I want it to have a middle Eastern/ Arabic look if possible.
Thanks :)
Target Market(s)
Butchers
Restaurants
Industry/Entity Type
Business
Contact Information for Business Card
Business name: Zarqa fowl
Business tag line: "The Tender Path"
E-mail: zarqa_fowl@mailbox-example.com
Name: Tariq Moussef

```html
<!DOCTYPE html>
<html lang="en">
<head>
<meta charset="utf-8">
<title>Zarqa Fowl — Business Card</title>
<link rel="stylesheet" href="https://fonts.googleapis.com/css2?family=Crimson+Pro:wght@400;700;800&display=swap">
<style>
  :root {
    --backdrop: #33434b;
    --card-black: #0c0c0d;
    --card-red: #b0282b;
    --ink-white: #ffffff;
    --ink-soft: #e8e8e8;
  }
  * { margin: 0; padding: 0; box-sizing: border-box; }
  html, body {
    width: 1200px;
    height: 900px;
    overflow: hidden;
    background: var(--backdrop);
    font-family: "Crimson Pro", Georgia, serif;
  }
  .stage {
    width: 1200px;
    height: 900px;
    display: flex;
    align-items: center;
    justify-content: center;
  }
  .business-card {
    position: relative;
    width: 900px;
    height: 514px;
    background: var(--card-black);
    overflow: hidden;
    box-shadow: 0 18px 40px rgba(0, 0, 0, 0.35);
  }
  .red-field {
    position: absolute;
    inset: 0;
    width: 900px;
    height: 514px;
  }
  .red-field path { fill: var(--card-red); }

  .brand {
    position: absolute;
    left: 60px;
    top: 34px;
    color: var(--ink-white);
  }
  .brand-name {
    display: flex;
    align-items: center;
    gap: 10px;
    font-weight: 700;
    font-size: 30px;
    line-height: 1;
  }
  .brand-mark {
    width: 14px;
    height: 14px;
    border: 2px solid var(--ink-white);
  }
  .brand-tagline {
    margin-top: 6px;
    font-weight: 700;
    font-size: 16px;
    letter-spacing: 0.06em;
    text-transform: uppercase;
  }

  .holder-name {
    position: absolute;
    left: 60px;
    top: 168px;
    color: var(--ink-white);
    font-weight: 700;
    font-size: 24px;
  }

  .contact-list {
    position: absolute;
    left: 56px;
    top: 222px;
    list-style: none;
    color: var(--ink-soft);
  }
  .contact-item {
    display: flex;
    align-items: center;
    gap: 10px;
    height: 34px;
    font-weight: 700;
    font-size: 17px;
  }
  .contact-icon {
    width: 20px;
    height: 20px;
    flex: none;
  }

  .hero-name {
    position: absolute;
    left: 470px;
    top: 250px;
    color: var(--ink-white);
    font-weight: 800;
    font-size: 118px;
    line-height: 0.92;
    letter-spacing: 0.01em;
    white-space: nowrap;
  }
</style>
</head>
<body>
<main class="stage">
  <article class="business-card">
    <svg class="red-field" viewBox="0 0 900 514" aria-hidden="true">
      <path d="M545 0 Q470 330 305 514 L900 514 L900 0 Z"/>
    </svg>

    <header class="brand">
      <div class="brand-name"><span class="brand-mark"></span>Zarqa Fowl</div>
      <div class="brand-tagline">The Tender Path</div>
    </header>

    <h1 class="holder-name">Tariq Moussef</h1>

    <ul class="contact-list">
      <li class="contact-item">
        <svg class="contact-icon" viewBox="0 0 24 24" aria-hidden="true">
          <path fill="#fff" d="M6.6 10.8c1.4 2.8 3.8 5.1 6.6 6.6l2.2-2.2c.3-.3.7-.4 1-.2 1.1.4 2.3.6 3.6.6.6 0 1 .4 1 1V20c0 .6-.4 1-1 1C10.6 21 3 13.4 3 4c0-.6.4-1 1-1h3.5c.6 0 1 .4 1 1 0 1.3.2 2.5.6 3.6.1.3 0 .7-.2 1l-2.3 2.2z"/>
        </svg>
        07812450937
      </li>
      <li class="contact-item">
        <svg class="contact-icon" viewBox="0 0 24 24" aria-hidden="true">
          <circle cx="12" cy="12" r="9" fill="none" stroke="#fff" stroke-width="2"/>
          <path d="M3 12h18M12 3c3 3 3 15 0 18M12 3c-3 3-3 15 0 18" fill="none" stroke="#fff" stroke-width="1.5"/>
        </svg>
        www.zarqafowl-example.com
      </li>
      <li class="contact-item">
        <svg class="contact-icon" viewBox="0 0 24 24" aria-hidden="true">
          <rect x="2.5" y="5.5" width="19" height="13" fill="none" stroke="#fff" stroke-width="1.6"/>
          <path d="M2.5 5.5l9.5 7.5 9.5-7.5" fill="none" stroke="#fff" stroke-width="1.6"/>
        </svg>
        zarqa_fowl@mailbox-example.com
      </li>
    </ul>

    <div class="hero-name">Zarqa<br>Fowl</div>
  </article>
</main>
</body>
</html>
```